Rovi is a not-for-profit college planning organization serving the students of Louisiana's public and private schools. This contest is one of many scholarship opportunities that we will offer to the Senior High School Class of 2014. This flyer design will be distributed to all high school seniors, encouraging them to submit a drawing, painting or graphic design using the theme "Louisiana Holiday Cheer and Happy New Year". The winning student design will be used on our organization's Holiday Greeting Card and will be mailed in December of 2012 to all of our clients.
This design will be printed as an 8-1/2" x 11" flyer.
A copy of last year's winning flyer is attached for your use in creating a 2013 Winter Sketch Challenge Flyer. The deadline will be November 1, 2013.
This flyer will be distributed to Louisiana high school seniors which will range from 17-18 years old.

```html
<!DOCTYPE html>
<html lang="en">
<head>
<meta charset="utf-8">
<title>Rovi — Winter Sketch Challenge Flyer</title>
<link rel="stylesheet" href="https://fonts.googleapis.com/css2?family=Andika:wght@700&family=Arimo:wght@400;700&family=Chewy&family=Oswald:wght@700&display=swap">
<style>
  :root {
    --paper: #ffffff;
    --ink-gray: #3a3a3a;
    --ink-dark: #1c1c1c;
    --navy: #2b3a8f;
    --red: #d9262b;
    --badge-red: #c4161c;
    --yellow: #f4e23a;
    --orange: #f39a1e;
    --green: #8dc63f;
    --green-text: #3aa13a;
    --halo: #f1f1f1;
  }
  * { margin: 0; padding: 0; box-sizing: border-box; }
  html, body { width: 988px; height: 1200px; overflow: hidden; background: var(--paper); }
  .flyer { position: relative; width: 988px; height: 1200px; background: var(--paper); overflow: hidden; font-family: "Arimo", Arial, sans-serif; }

  .swoosh { position: absolute; left: 0; top: 0; width: 988px; height: 640px; }

  .brand { position: absolute; left: 60px; top: 0; width: 300px; text-align: center; }
  .brand-halo { position: absolute; left: 10px; top: 20px; width: 280px; height: 280px; border-radius: 50%; background: var(--halo); }
  .brand-mark { position: relative; display: flex; align-items: center; justify-content: center; gap: 12px; padding-top: 140px; }
  .brand-dot { width: 56px; height: 56px; border-radius: 50%; background: var(--green); }
  .brand-name { font-weight: 700; font-size: 64px; color: var(--ink-gray); line-height: 1; }
  .brand-tagline { position: relative; margin-top: 58px; font-size: 15px; line-height: 1.3; color: var(--ink-dark); }

  .contest-title { position: absolute; right: 32px; top: 128px; font-family: "Oswald", Impact, sans-serif; font-weight: 700; font-size: 48px; letter-spacing: 0.5px; line-height: 1.1; color: var(--ink-gray); text-transform: uppercase; white-space: nowrap; }

  .theme-badge { position: absolute; left: 410px; top: 212px; width: 270px; height: 270px; }
  .theme-badge svg { position: absolute; inset: 0; }
  .badge-text { position: absolute; inset: 0; display: flex; flex-direction: column; align-items: center; padding-top: 40px; text-align: center; }
  .badge-year { font-family: "Chewy", "Comic Sans MS", cursive; font-size: 56px; color: #fff; line-height: 1; }
  .badge-theme { font-family: "Chewy", "Comic Sans MS", cursive; font-size: 58px; color: var(--yellow); line-height: 0.95; }
  .badge-deadline { font-size: 16px; font-weight: 700; color: #fff; line-height: 1.2; margin-top: 4px; }

  .contact { position: absolute; left: 60px; top: 520px; color: #fff; transform: rotate(-8deg); transform-origin: left top; white-space: nowrap; }
  .contact-label { font-size: 28px; line-height: 1.1; }
  .contact-phone { font-size: 34px; font-weight: 700; line-height: 1.15; }

  .theme-heading { position: absolute; right: 52px; top: 462px; text-align: right; font-family: "Andika", "Trebuchet MS", sans-serif; font-weight: 700; font-size: 58px; line-height: 1.07; color: var(--navy); }

  .brush-art { position: absolute; left: 110px; top: 640px; width: 240px; height: 150px; border-radius: 40px; background: radial-gradient(circle at 55% 60%, #f2b36a 0%, #f6d9b0 45%, rgba(255,255,255,0) 75%); }

  .entry-types { position: absolute; right: 60px; top: 668px; text-align: right; font-family: "Andika", "Trebuchet MS", sans-serif; font-weight: 700; font-size: 36px; line-height: 1.3; color: var(--ink-dark); }

  .prize-note { position: absolute; left: 0; right: 0; top: 812px; padding-left: 60px; text-align: center; font-weight: 700; font-size: 22px; line-height: 1.4; color: var(--red); }

  .scholarship-note { position: absolute; left: 0; right: 0; top: 892px; padding-right: 20px; text-align: center; font-weight: 700; font-size: 18px; line-height: 1.35; color: var(--green-text); }
  .scholarship-note strong { font-size: 26px; }

  .paint-art { position: absolute; left: 0; top: 965px; width: 640px; height: 235px; background: linear-gradient(170deg, rgba(255,255,255,0) 0%, #f6d6c8 35%, #e88a5c 55%, #c9e59a 80%, #7cc242 100%); }
  .student-photo { position: absolute; left: 628px; top: 975px; width: 352px; height: 200px; border-radius: 26px; background: linear-gradient(135deg, #e9e2da 0%, #c9b6a4 50%, #8c7a6a 100%); }
  .grass-strip { position: absolute; left: 0; right: 0; bottom: 0; height: 34px; background: linear-gradient(180deg, #9bd34f, #5fa82a); }
</style>
</head>
<body>
<main class="flyer">

  <svg class="swoosh" viewBox="0 0 988 640" aria-hidden="true">
    <path d="M0 428 C 200 413 380 423 540 373 C 700 318 840 263 988 243" fill="none" stroke="var(--orange)" stroke-width="30"/>
    <path d="M0 455 C 200 440 380 450 540 400 C 700 345 840 290 988 270" fill="none" stroke="var(--red)" stroke-width="40"/>
    <path d="M0 478 C 200 463 380 473 540 423 C 700 368 840 313 988 293" fill="none" stroke="var(--yellow)" stroke-width="8"/>
    <path d="M0 482 C 200 467 380 477 545 425 Q 440 570 300 610 L 0 630 Z" fill="var(--green)"/>
  </svg>

  <header class="brand">
    <div class="brand-halo"></div>
    <div class="brand-mark">
      <span class="brand-dot"></span>
      <span class="brand-name">Rovi</span>
    </div>
    <p class="brand-tagline">Louisiana's Non-Profit Resource<br>for College Planning</p>
  </header>

  <h1 class="contest-title">Winter Sketch Challenge</h1>

  <div class="theme-badge">
    <svg viewBox="0 0 270 270" aria-hidden="true">
      <g fill="var(--yellow)">
        <circle cx="135" cy="125" r="100"/>
        <circle cx="135" cy="35" r="42"/><circle cx="205" cy="62" r="42"/><circle cx="230" cy="130" r="42"/>
        <circle cx="200" cy="198" r="42"/><circle cx="70" cy="198" r="42"/>
        <circle cx="40" cy="130" r="42"/><circle cx="65" cy="62" r="42"/>
        <path d="M112 225 L 140 268 L 165 222 Z"/>
      </g>
      <g fill="var(--badge-red)">
        <circle cx="135" cy="125" r="94"/>
        <circle cx="135" cy="35" r="36"/><circle cx="205" cy="62" r="36"/><circle cx="230" cy="130" r="36"/>
        <circle cx="200" cy="198" r="36"/><circle cx="70" cy="198" r="36"/>
        <circle cx="40" cy="130" r="36"/><circle cx="65" cy="62" r="36"/>
        <path d="M118 222 L 140 258 L 160 220 Z"/>
      </g>
    </svg>
    <div class="badge-text">
      <span class="badge-year">2013</span>
      <span class="badge-theme">theme</span>
      <span class="badge-deadline">The deadline<br>will be November<br>1, 2013</span>
    </div>
  </div>

  <div class="contact">
    <div class="contact-label">Contact Us</div>
    <div class="contact-phone">800 -555-0142</div>
  </div>

  <h2 class="theme-heading">Louisiana<br>Holiday Cheer<br>&amp; Happy New Year</h2>

  <div class="brush-art" role="img" aria-label="Illustration of a paintbrush with colourful paint splashes"></div>

  <p class="entry-types">All students can submit a drawing<br>painting, or graphic design</p>

  <p class="prize-note">The winning student design will be used on our organization's Holiday<br>Greeting Card and will be mailed in December of 2012 to all of our clients</p>

  <p class="scholarship-note">This contest is one of many <strong>Scholarship opportunities</strong><br>that we will offer to the Senior High School Class of 2014</p>

  <div class="paint-art" role="img" aria-label="Illustration of paintbrushes, spilled red paint, a red poppy and grass"></div>
  <div class="grass-strip"></div>
  <div class="student-photo" role="img" aria-label="Photo of a smiling student drawing at a desk"></div>

</main>
</body>
</html>
```